Harlow Auto , a Dealership and Repair Shop in Brenton Iowa

Harlow Auto is a repair shop and auto sales dealership that offers oil changes, alignments, tires, air conditioning work, computer diagnostics. Focused on Vantras, Marlo and Brisk. Small business with less than 10 employees. Billboard sign is in town and not the larger billboard
billboard is 8ft x 18ft

Target Market(s)

General public

Industry/Entity Type

automotive

Font styles to use
Serif
Sans Serif

Colors

Designer to choose colors to be used in the design.

Requirements
Must have
• Located 2 miles north of Brenton. Sales and service. Phone number 319-555-0187
Nice to have
• Picture of a car or truck, or both. picture of wrench
Should not have
• Not sure

```html
<!DOCTYPE html>
<html lang="en">
<head>
<meta charset="UTF-8">
<title>Harlow Auto – Roadside Sign</title>
<link href="https://fonts.googleapis.com/css2?family=Outfit:wght@300;400;600;700&display=swap" rel="stylesheet">
<style>
  :root {
    --page-bg: #d6d6d6;
    --sign-blue: #0540b5;
    --logo-band: #073ba8;
    --accent-yellow: #ffcc00;
    --ink-white: #ffffff;
    --photo-teal: #18c9b4;
    --photo-deep: #0a5ab8;
  }
  * { margin: 0; padding: 0; box-sizing: border-box; }
  html, body { width: 1200px; height: 1200px; overflow: hidden; }
  body {
    background: var(--page-bg);
    font-family: "Outfit", "Helvetica Neue", Arial, sans-serif;
    position: relative;
  }
  .sign {
    position: absolute;
    left: 345px; top: 40px;
    width: 510px; height: 1120px;
    background: var(--sign-blue);
    overflow: hidden;
  }
  .brand {
    position: absolute;
    left: 83px; top: 52px;
    width: 367px; height: 168px;
    background: var(--logo-band);
    display: flex; align-items: center; justify-content: center;
  }
  .brand-name {
    color: var(--ink-white);
    font-weight: 700;
    font-size: 60px;
    letter-spacing: 1px;
  }
  .location-frame {
    position: absolute;
    left: 0; top: 0;
    width: 510px; height: 620px;
  }
  .line {
    position: absolute;
    left: 0; width: 100%;
    text-align: center;
    line-height: 1;
    white-space: nowrap;
  }
  .headline { font-weight: 600; font-size: 66px; color: var(--ink-white); }
  .headline.highlight { color: var(--accent-yellow); }
  .frame-gap {
    display: inline-block;
    background: var(--sign-blue);
    padding: 0 14px;
  }
  .services { font-weight: 300; font-size: 54px; color: var(--ink-white); letter-spacing: 1px; }
  .phone {
    font-weight: 600; font-size: 56px; color: var(--accent-yellow);
    display: flex; align-items: center; justify-content: center; gap: 16px;
  }
  .phone-icon { width: 38px; height: 38px; }
  .truck-scene {
    position: absolute;
    left: 0; top: 912px;
    width: 510px; height: 208px;
    background:
      radial-gradient(ellipse 60% 70% at 55% 75%, rgba(24,201,180,0.85), rgba(24,201,180,0) 70%),
      linear-gradient(180deg, var(--sign-blue) 0%, var(--photo-deep) 55%, #0b3f8f 100%);
  }
</style>
</head>
<body>
  <div class="sign">
    <div class="brand">
      <span class="brand-name">Harlow Auto</span>
    </div>

    <svg class="location-frame" viewBox="0 0 510 620" aria-hidden="true">
      <path d="M38 575 V271 H472 V575 Z" fill="none" stroke="#ffffff" stroke-width="6"/>
    </svg>

    <div class="line headline" style="top:307px;">LOCATED</div>
    <div class="line headline highlight" style="top:386px;">2 MILES</div>
    <div class="line headline" style="top:464px;">NORTH OF</div>
    <div class="line headline highlight" style="top:543px;"><span class="frame-gap">BRENTON</span></div>

    <div class="line services" style="top:648px;">SALES AND</div>
    <div class="line services" style="top:710px;">SERVICE</div>

    <div class="line phone" style="top:824px;">
      <svg class="phone-icon" viewBox="0 0 38 38" aria-hidden="true">
        <rect width="38" height="38" rx="6" fill="#ffcc00"/>
        <path d="M12 9c1-1 2.5-1 3.3.2l2.2 3.4c.6 1 .4 2.2-.5 2.9l-1.4 1.1c1.2 2.6 3.2 4.6 5.8 5.8l1.1-1.4c.7-.9 1.9-1.1 2.9-.5l3.4 2.2c1.2.8 1.2 2.3.2 3.3l-1.6 1.6c-1.4 1.4-3.6 1.8-5.4.8C16.4 26 12 21.6 9.6 16c-1-1.8-.6-4 .8-5.4z" fill="#0540b5"/>
      </svg>
      <span>319-555-0187</span>
    </div>

    <div class="truck-scene" role="img" aria-label="Photo of a semi truck with a container trailer on a highway, tinted teal and blue"></div>
  </div>
</body>
</html>
```